Unique business card design

We are looking for a design that reflects our unique social media and online marketing agency "Kelvora Media". We are a young agency with a focus on speakers, coaches and trainers. In other words, we support people who want to do good with their work and help other people live a happier, more successful and fulfilling life, reach as many people as possible with their work and thus have an influence. Our values are: sustainability, creating added value, individuality, proactivity. We want our clients to feel comfortable with us and that's why the relationship with them is very important to us. We want every customer to become a lifelong friend of the company. Most of our clients are premium coaches, meaning they are in the higher priced segment and expect seriousness, professionalism and quality. All of these things should reflect our business card as well. I look forward to feedback. Best regards, Dorian Whitcombe
Look and feel
Each slider illustrates characteristics of the customer's brand and the style your logo design should communicate.

```html
<!DOCTYPE html>
<html lang="en">
<head>
<meta charset="utf-8">
<title>Kelvora Media – Business Cards</title>
<link rel="stylesheet" href="https://fonts.googleapis.com/css2?family=Open+Sans:wght@400;600&display=swap">
<style>
  :root {
    --backdrop: #2b2724;
    --card: #0e0e10;
    --card-edge: #1a1a1d;
    --brand-blue: #2f7fd8;
    --deep-blue: #2a2fa0;
    --tagline: #3c3cc0;
    --text: #cfcfd2;
    --divider: #2c2c30;
  }
  * { box-sizing: border-box; margin: 0; padding: 0; }
  html, body {
    width: 1200px; height: 844px; overflow: hidden;
    background: var(--backdrop);
    font-family: "Open Sans", Arial, sans-serif;
  }
  .stage {
    position: relative; width: 1200px; height: 844px;
    display: flex; align-items: center; justify-content: center; gap: 50px;
  }
  .card {
    width: 525px; height: 300px;
    background: var(--card);
    border: 1px solid var(--card-edge);
    box-shadow: 0 14px 30px rgba(0,0,0,.45);
    position: relative;
    display: flex; align-items: center;
  }
  .brand { display: flex; flex-direction: column; align-items: flex-start; gap: 8px; }
  .brand-row { display: flex; align-items: center; gap: 12px; }
  .brand-square { width: 46px; height: 46px; background: var(--brand-blue); }
  .brand-name { font-size: 30px; font-weight: 400; color: var(--brand-blue); letter-spacing: .5px; line-height: 1; }
  .brand-tagline { font-size: 12.5px; color: var(--tagline); letter-spacing: 1.6px; padding-left: 2px; }

  /* back: logo + contact */
  .card--back { padding: 0 0 0 40px; }
  .card--back .brand { width: 250px; }
  .card--back .brand-name { font-size: 24px; }
  .card--back .brand-square { width: 38px; height: 38px; }
  .card--back .brand-tagline { font-size: 10.5px; letter-spacing: 1.2px; }
  .divider { width: 1px; align-self: stretch; margin: 40px 28px 40px 6px; background: var(--divider); }
  .contact { color: var(--text); font-size: 12.5px; line-height: 1.55; }
  .person { font-size: 17px; font-weight: 600; color: var(--brand-blue); line-height: 1.2; }
  .person .first { color: var(--deep-blue); }
  .role { font-size: 12.5px; margin-bottom: 6px; }
  .contact-list { list-style: none; }
  .contact-list li { display: flex; align-items: center; gap: 8px; }
  .contact-list svg { width: 11px; height: 11px; fill: var(--brand-blue); flex: none; }
  .address { margin-top: 6px; }

  /* front: centred logo */
  .card--front { justify-content: center; }
</style>
</head>
<body>
<main class="stage">
  <section class="card card--back" aria-label="Business card, contact side">
    <div class="brand">
      <div class="brand-row">
        <span class="brand-square"></span>
        <span class="brand-name">Kelvora Media</span>
      </div>
      <span class="brand-tagline">Online Marketing Services</span>
    </div>
    <div class="divider"></div>
    <div class="contact">
      <p class="person"><span class="first">Dorian</span> Whitcombe</p>
      <p class="role">Managing Director</p>
      <ul class="contact-list">
        <li><svg viewBox="0 0 12 12"><path d="M1 4c0-2 2-3 5-3s5 1 5 3l-2 1-1-1.5H4L3 5zM2 6h8l1 5H1z"/></svg>044-555 018 274</li>
        <li><svg viewBox="0 0 12 12"><path d="M3 0h6a1 1 0 0 1 1 1v10a1 1 0 0 1-1 1H3a1 1 0 0 1-1-1V1a1 1 0 0 1 1-1zm0 2v7h6V2z"/></svg>044-555 018 274</li>
        <li><svg viewBox="0 0 12 12"><path d="M0 2h12v1L6 7 0 3zm0 2.5 6 4 6-4V10H0z"/></svg>info@kelvoramedia.com</li>
        <li><svg viewBox="0 0 12 12"><circle cx="6" cy="6" r="5.5"/></svg>www.kelvoramedia.com</li>
      </ul>
      <p class="address">48 Harbour Lane, Westbury<br>Northland, 104822.</p>
    </div>
  </section>

  <section class="card card--front" aria-label="Business card, logo side">
    <div class="brand">
      <div class="brand-row">
        <span class="brand-square"></span>
        <span class="brand-name">Kelvora Media</span>
      </div>
      <span class="brand-tagline">Online Marketing Services</span>
    </div>
  </section>
</main>
</body>
</html>
```